依頼詳細
写真・ビデオの撮影・編集および写真スタジオを行っています。お客様にお送りする封筒のデザインをお願いします。かっこよく・爽やかなイメージでお願いします。封筒の下位置部分のレイアウトでお願いします。。
記載項目
法人名/住所/電話/Fax/ホームページアドレス+ロゴ
希望イメージ
シンプル 複雑
単色 カラフル
暗い 明るい
日常 高級
遊び心 厳粛
未来的 伝統的
女性的 男性的
希望する色
青系、水色系、緑系
納品ファイル
• フォトショップ形式 (.psd)
補足説明
素材のロゴデータのロゴ部分と文字部分のバランスはおまかせ致します。
封筒の色は白色で考えております。よろしくお願い致します。

```html
<!DOCTYPE html>
<html lang="ja">
<head>
<meta charset="utf-8">
<title>株式会社ルミフレーム 封筒</title>
<link rel="stylesheet" href="https://fonts.googleapis.com/css2?family=Noto+Sans+JP:wght@400;500;700&display=swap">
<style>
  :root {
    --paper: #ffffff;
    --outline: #9a9a9a;
    --ink: #2b2b2b;
    --film-blue: #2f7fd6;
    --film-light: #cfe3f8;
  }
  html, body {
    margin: 0;
    padding: 0;
    width: 765px;
    height: 1200px;
    overflow: hidden;
    background: var(--paper);
  }
  .envelope {
    position: relative;
    width: 765px;
    height: 1200px;
    font-family: "Noto Sans JP", sans-serif;
    color: var(--ink);
  }
  .envelope-shape {
    position: absolute;
    inset: 0;
  }
  .film-band {
    position: absolute;
    left: 0;
    width: 765px;
  }
  .film-band--upper { top: 872px; }
  .film-band--lower { top: 1108px; }
  .brand {
    position: absolute;
    left: 88px;
    top: 960px;
  }
  .brand-mark {
    width: 58px;
    height: 58px;
    box-sizing: border-box;
    border: 5px solid var(--ink);
    margin-bottom: 16px;
  }
  .brand-name {
    font-weight: 700;
    font-size: 33px;
    letter-spacing: 3px;
    line-height: 1;
  }
  .sender {
    position: absolute;
    left: 440px;
    top: 925px;
    font-size: 17px;
    line-height: 25px;
    font-weight: 500;
  }
  .sender-company {
    font-weight: 700;
    font-size: 19px;
    margin: 0 0 16px;
  }
  .sender-details {
    margin: 0;
  }
</style>
</head>
<body>
  <div class="envelope">
    <svg class="envelope-shape" width="765" height="1200" viewBox="0 0 765 1200">
      <path d="M30 1 L735 1 L764 128 L764 1199 L1 1199 L1 128 Z" fill="var(--paper)" stroke="var(--outline)" stroke-width="2"/>
      <line x1="1" y1="128" x2="764" y2="128" stroke="var(--outline)" stroke-width="1"/>
    </svg>

    <svg class="film-band film-band--upper" width="765" height="52" viewBox="0 0 765 52">
      <path d="M0 14 C190 0 380 0 570 8 C650 12 720 10 765 6 L765 40 C720 44 650 46 570 42 C380 34 190 34 0 48 Z" fill="var(--film-blue)"/>
      <path d="M0 22 C190 9 380 9 570 17 C650 21 720 19 765 15 L765 31 C720 35 650 37 570 33 C380 25 190 25 0 39 Z" fill="var(--film-light)"/>
    </svg>

    <div class="brand">
      <div class="brand-mark"></div>
      <div class="brand-name">LUMIFRAME</div>
    </div>

    <div class="sender">
      <p class="sender-company">株式会社ルミフレーム</p>
      <p class="sender-details">
        〒530-0012<br>
        大阪府大阪市北区芝田町 8-21<br>
        電話 06-6000-2480<br>
        Fax<br>
        https://lumiframe-studio.jp/
      </p>
    </div>

    <svg class="film-band film-band--lower" width="765" height="52" viewBox="0 0 765 52">
      <path d="M0 6 C120 2 260 4 400 12 C540 20 660 18 765 10 L765 44 C660 52 540 54 400 46 C260 38 120 36 0 40 Z" fill="var(--film-blue)"/>
      <path d="M0 15 C120 11 260 13 400 21 C540 29 660 27 765 19 L765 35 C660 43 540 45 400 37 C260 29 120 27 0 31 Z" fill="var(--film-light)"/>
    </svg>
  </div>
</body>
</html>
```